MOLT - Monitoring Natural Hazards from Space Web Application

KORVEN Sarl is a Luxembourg based Space-Startup that works in the field of Earth Observation. KORVEN is a platform able to extract value-added information from satellite data and is specialized in mapping Natural Disaster (floods, fires etc).

We are now developing a new vertical tool, called MOLT, dedicated to the monitoring of natural hazards in Humanitarian Camps around the world.

The goal of MOLT is to hide to the users' all the complexity of the Satellite Image processing and just provide them the results.

This project require to Design 4 pages of MOLT:
• Public Home Page (Code - V01)
• Dashboard (private Home Page) (Code - V03)
• Monitor (web GIS) (Code - V14)
• Registration Page (Code - V04)

We would like to provide the required time to make a good job.

Target Market(s)

Humanitarian Agencies, Goverments

Coding

Coded - Design and coding required

Number of Pages Required

4 page

Font styles to use
Other font styles liked:
• see the manual attached

Requirements
Must have
• 4 pages. One Home, one form, one dashboard and one web map.
Nice to have
• Please read the attachment with all the detailed instructions

```html
<!DOCTYPE html>
<html lang="en">
<head>
<meta charset="utf-8">
<title>Register in Molt</title>
<link href="https://fonts.googleapis.com/css2?family=Poppins:wght@400;500;600;700&display=swap" rel="stylesheet">
<style>
  :root {
    --ink: #224a55;
    --accent: #ebb43d;
    --field: #f2f3f4;
    --bg: #ffffff;
  }
  * { box-sizing: border-box; margin: 0; padding: 0; }
  html, body { width: 1200px; height: 756px; overflow: hidden; background: var(--bg); }
  body { font-family: "Poppins", sans-serif; color: var(--ink); position: relative; }

  .brand-mark {
    position: absolute; left: 114px; top: 56px; width: 92px; height: 92px;
    border: 3px solid var(--accent); border-radius: 50%;
    display: flex; align-items: center; justify-content: center;
    font-weight: 600; font-size: 20px; color: var(--accent); letter-spacing: 1px;
  }
  .page-title {
    position: absolute; left: 229px; top: 68px;
    font-size: 46px; font-weight: 700; line-height: 60px; letter-spacing: -0.3px;
  }
  .page-title .highlight { color: var(--accent); }

  .field-label {
    position: absolute; font-size: 11.5px; font-weight: 600; text-transform: uppercase;
    line-height: 14px; white-space: nowrap;
  }
  .field-label .required { color: var(--accent); }
  .field-input {
    position: absolute; height: 53px; background: var(--field); border-radius: 27px;
  }
  .field-input.select::after {
    content: ""; position: absolute; right: 30px; top: 21px;
    width: 6px; height: 6px; border-right: 1.6px solid var(--ink); border-bottom: 1.6px solid var(--ink);
    transform: rotate(45deg);
  }

  .address-panel {
    position: absolute; left: 751px; top: 193px; width: 335px; height: 412px;
    border: 1.5px solid var(--ink); border-radius: 12px;
  }
  .address-title {
    position: absolute; left: 783px; top: 180px; padding: 0 14px; background: var(--bg);
    font-size: 18px; font-weight: 600; line-height: 26px;
  }

  .consent {
    position: absolute; left: 114px; display: flex; align-items: center; gap: 11px;
    font-size: 12.5px; line-height: 14px;
  }
  .consent .box {
    width: 12px; height: 12px; border: 2px solid var(--ink); border-radius: 2px;
  }

  .register-button {
    position: absolute; left: 814px; top: 652px; width: 272px; height: 56px;
    background: var(--accent); border-radius: 28px; box-shadow: 0 2px 0 #d49d2a;
    display: flex; align-items: center; justify-content: center;
    font-size: 16px; font-weight: 700; letter-spacing: 0.3px;
  }
</style>
</head>
<body>
  <div class="brand-mark">MOLT</div>
  <h1 class="page-title">Register in <span class="highlight">Molt</span></h1>

  <!-- Personal column -->
  <div class="field-label" style="left:113px;top:192px">User ID<span class="required">*</span></div>
  <div class="field-input" style="left:114px;top:213px;width:273px"></div>
  <div class="field-label" style="left:113px;top:277px">Password<span class="required">*</span></div>
  <div class="field-input" style="left:114px;top:299px;width:273px"></div>
  <div class="field-label" style="left:113px;top:361px">Confirm Password<span class="required">*</span></div>
  <div class="field-input" style="left:114px;top:382px;width:273px"></div>
  <div class="field-label" style="left:113px;top:444px">Name<span class="required">*</span></div>
  <div class="field-input" style="left:114px;top:465px;width:273px"></div>
  <div class="field-label" style="left:113px;top:529px">Surname<span class="required">*</span></div>
  <div class="field-input" style="left:114px;top:550px;width:273px"></div>

  <!-- Contact & organization column -->
  <div class="field-label" style="left:431px;top:192px">Mobile Number<span class="required">*</span></div>
  <div class="field-input" style="left:432px;top:213px;width:273px"></div>
  <div class="field-label" style="left:431px;top:277px">E-mail<span class="required">*</span></div>
  <div class="field-input" style="left:432px;top:299px;width:273px"></div>
  <div class="field-label" style="left:431px;top:361px">Confirm E-mail<span class="required">*</span></div>
  <div class="field-input" style="left:432px;top:382px;width:273px"></div>
  <div class="field-label" style="left:431px;top:444px">Organization Name<span class="required">*</span></div>
  <div class="field-input" style="left:432px;top:465px;width:273px"></div>
  <div class="field-label" style="left:431px;top:529px">Organization Type<span class="required">*</span></div>
  <div class="field-input select" style="left:432px;top:550px;width:273px"></div>

  <!-- Organization address -->
  <div class="address-panel"></div>
  <div class="address-title">Organization Address</div>
  <div class="field-label" style="left:785px;top:240px">Street<span class="required">*</span></div>
  <div class="field-input" style="left:786px;top:261px;width:176px"></div>
  <div class="field-label" style="left:972px;top:240px">No<span class="required">*</span></div>
  <div class="field-input" style="left:972px;top:261px;width:86px"></div>
  <div class="field-label" style="left:785px;top:325px">Postal Code<span class="required">*</span></div>
  <div class="field-input" style="left:786px;top:347px;width:130px"></div>
  <div class="field-label" style="left:928px;top:325px">City<span class="required">*</span></div>
  <div class="field-input" style="left:928px;top:347px;width:130px"></div>
  <div class="field-label" style="left:785px;top:409px">Phone<span class="required">*</span></div>
  <div class="field-input" style="left:786px;top:430px;width:272px"></div>
  <div class="field-label" style="left:785px;top:494px">Country<span class="required">*</span></div>
  <div class="field-input select" style="left:786px;top:516px;width:272px"></div>

  <!-- Consent -->
  <div class="consent" style="top:657px"><span class="box"></span>I have read and Accept the MOLT Terms and Conditions</div>
  <div class="consent" style="top:686px"><span class="box"></span>I have read and Aeccpt the MOLT privacy Policy</div>

  <div class="register-button">REGISTER</div>
</body>
</html>
```